Exterior cleaning company requires a eye catching a5 leaflet

we need some updated leaflet designs, a5 folded, we are targeting all exterior cleaning contracts, including roof cleaning & treatment, render cleaning & Treatment, driveways, block paving cleaning using the latest in low pressure cleaning technologies along side high pressure jetwashing. gutter clearance and flushing, water fed telescopic pole window cleaning of difficult to reach windows and high buildings. our website : www.tkbellowsec.co.uk facebook page: https://www.facebook.com/tkbellowsexteriorcareltd Instagram: https://www.instagram.com/tkbellowsec/ a quick google search of roof cleaning, soft washing etc will provide results of what we are doing

Target Market(s)

home owners, commercial clients

Font styles to use
Serif
Sans Serif

Requirements
Must have
• A5 Landscape folded leaflet, front page with company information and bullet points of main works : window & conservatory cleaning, roof cleaning & treatment, Render cleaning & treatment, pressure washing, soft washing, gutter clearing, pressure washing of patios, driveways, gutters, fascias (more info can be provided on techniques etc if required)

```html
<!DOCTYPE html>
<html lang="en">
<head>
<meta charset="utf-8">
<title>T.K Bellows Exterior Care – Our Services</title>
<link href="https://fonts.googleapis.com/css2?family=Bebas+Neue&family=Questrial&display=swap" rel="stylesheet">
<style>
  :root {
    --frame-grey: #8e908f;
    --heading-grey: #8a8c8b;
    --body-grey: #9a9c9b;
    --emblem-light: #eceded;
    --emblem-mid: #d9dad9;
    --paper: #ffffff;
  }
  * { margin: 0; padding: 0; box-sizing: border-box; }
  html, body { width: 1200px; height: 927px; overflow: hidden; background: var(--paper); }
  .leaflet-panel {
    position: relative;
    width: 1200px;
    height: 927px;
    background: var(--paper);
    overflow: hidden;
    font-family: "Questrial", "Helvetica Neue", Arial, sans-serif;
  }
  .frame-top {
    position: absolute; left: 0; top: 0;
    width: 1200px; height: 31px;
    background: var(--frame-grey);
  }
  .frame-left {
    position: absolute; left: 0; top: 0;
    width: 30px; height: 927px;
    background: var(--frame-grey);
  }
  .emblem-area {
    position: absolute; left: 30px; top: 31px;
    width: 384px; height: 385px;
    background: linear-gradient(160deg, var(--emblem-light), var(--emblem-mid));
  }
  .section-title {
    position: absolute;
    font-family: "Bebas Neue", Impact, sans-serif;
    font-size: 41px;
    line-height: 1;
    letter-spacing: 0.5px;
    color: var(--frame-grey);
    font-weight: 400;
  }
  .services-title { left: 449px; top: 95px; }
  .about-title { left: 70px; top: 759px; }
  .service { position: absolute; width: 330px; }
  .service-name {
    font-size: 17px;
    line-height: 17px;
    font-weight: 400;
    color: var(--heading-grey);
    letter-spacing: 0.2px;
    margin-bottom: 11px;
    white-space: nowrap;
  }
  .service-text, .about-text {
    font-size: 13px;
    line-height: 20.4px;
    color: var(--body-grey);
    letter-spacing: 0.3px;
    white-space: nowrap;
  }
  .col-left { left: 449px; }
  .col-right { left: 849px; }
  .about-text { position: absolute; left: 70px; top: 810px; }
</style>
</head>
<body>
<main class="leaflet-panel">
  <div class="frame-top"></div>
  <div class="frame-left"></div>
  <div class="emblem-area" role="img" aria-label="Company window emblem"></div>

  <h1 class="section-title services-title">Our Services</h1>

  <section class="service col-left" style="top:165px">
    <h2 class="service-name">EXTERNAL WINDOWS</h2>
    <p class="service-text">Our staff use the reach &amp; washes system<br>otherwise known as the ‘water fed pole’. A<br>technique which compared to traditional<br>window cleaning, enabling us to reach your<br>windows and frames safely from the ground.</p>
  </section>

  <section class="service col-left" style="top:343px">
    <h2 class="service-name">INTERNAL WINDOWS</h2>
    <p class="service-text">We clean internal windows and mirrors using the<br>dragon fly system. This method also using<br>purified water can reach them hard to access<br>windows again safely from the ground.</p>
  </section>

  <section class="service col-left" style="top:498px">
    <h2 class="service-name">CONSERVATORY ROOFS</h2>
    <p class="service-text">Has your conservatory roof started to turn<br>green, full of bird muck or dirt? Our water pole<br>method 99% of the time gets rid of all the dirt<br>and grime build up that’s left on your roof.</p>
  </section>

  <section class="service col-left" style="top:653px">
    <h2 class="service-name">FASCIAS &amp; GUTTERS</h2>
    <p class="service-text">Using our telescopic pressure washing lance,<br>we can clean all of your UPVC fascia’s, gutters<br>and drain pipes safely from the ground. The end<br>result your fascia’s and gutters looking like<br>brand new again.</p>
  </section>

  <section class="service col-right" style="top:156px">
    <h2 class="service-name">SOLAR PANELS</h2>
    <p class="service-text">Using our access equipment we can clean your<br>solar panels. Anything that blocks the light<br>transmission to your solar PV (or thermal) panels<br>has the potential to lower the performance.</p>
  </section>

  <section class="service col-right" style="top:314px">
    <h2 class="service-name">PRESSURE WASHING</h2>
    <p class="service-text">We offer a wide range of pressure washing<br>services from garden furniture to house roofs at<br>competitive prices. Cleaning and restoration of<br>all hard surfaces in both the domestic and<br>commercial market.</p>
  </section>

  <section class="service col-right" style="top:490px">
    <h2 class="service-name">GUTTER CLEANING</h2>
    <p class="service-text">Your property's gutters and downpipes<br>accumulate all sorts of debris brought by the<br>wind. Using our high reach vac we can clean<br>the gutters safely from the ground eliminating<br>any falls from height.</p>
  </section>

  <section class="service col-right" style="top:653px">
    <h2 class="service-name">DRIVEWAYS &amp; PATIOS</h2>
    <p class="service-text">From small patio areas to large driveways we<br>clean it all. T.K Bellows specialise in all driveway<br>and patio cleaning from Indian stone, tarmac,<br>concrete flags to block paving.</p>
  </section>

  <h2 class="section-title about-title">About Us</h2>
  <p class="about-text">T.K Bellows Exterior Care is Southport’s most<br>reliable, professional cleaning company who<br>have been providing cleaning services across<br>the North West for 10 years!</p>
</main>
</body>
</html>
```